lab equipment website

We need a fresh new look for a company website called tarvio. We will be using the current logo and brand colors on their current website tarvio.com. They want to keep their text and on-page SEO, but would like to reformat it to look more modern and fresh. They want to have everything be high performance with a great user experience. Their main call to action is for people to fill in a contact form so they can call them. There is some information that is purposely above the fold on the instrument pages. I will need the home page, about page and a leasing page.

```html
<!DOCTYPE html>
<html lang="en">
<head>
<meta charset="utf-8">
<title>tarvio — Lab Equipment Leasing</title>
<link href="https://fonts.googleapis.com/css2?family=Open+Sans:wght@400;600;700&display=swap" rel="stylesheet">
<style>
:root{
  --dark:#2b2e34;
  --teal:#0f7670;
  --teal-bright:#17a096;
  --ink:#333;
  --muted:#666;
  --line:#d9dcdf;
  --white:#fff;
  --foot-text:#c8cbd0;
  --band-text:#dcefed;
}
*{box-sizing:border-box;margin:0;padding:0}
html,body{width:1200px;height:3836px;overflow:hidden}
body{font-family:"Open Sans",Arial,sans-serif;color:var(--ink);background:var(--white);position:relative}
.abs{position:absolute}
.btn{display:inline-block;background:var(--teal-bright);color:var(--white);font-size:14px;font-weight:600;padding:0 26px;height:34px;line-height:34px;border-radius:2px}
h2.section-title{font-size:30px;font-weight:700;text-align:center;color:var(--ink)}
p.body{font-size:13px;line-height:20px;color:var(--muted);margin-bottom:14px}

/* header */
.site-header{top:0;left:0;width:1200px;height:52px;background:var(--dark)}
.menu-icon{left:104px;top:18px}
.brand{left:148px;top:10px;display:flex;align-items:center;gap:8px;color:var(--white);font-size:24px;font-weight:700}
.brand-dot{width:22px;height:22px;border-radius:50%;background:var(--teal-bright)}
.social{display:flex;gap:8px}
.social span{width:20px;height:20px;border-radius:50%;background:var(--white)}
.social span.on{background:var(--teal-bright)}
.header-social{left:936px;top:16px}

/* hero */
.hero{top:52px;left:0;width:1200px;height:668px;background:linear-gradient(100deg,#c9d6de 0%,#e7edf0 35%,#aebdc6 60%,#7f909c 100%)}
.hero-title{left:264px;top:388px;color:var(--white);font-size:34px;font-weight:700;line-height:44px;letter-spacing:1px}
.hero-title span{display:block;padding-left:50px}
.consult{left:752px;top:168px;width:330px;height:356px;background:rgba(43,46,52,.88);padding:16px 24px}
.consult h3{color:var(--white);font-size:17px;font-weight:600;margin-bottom:14px}
.field{height:30px;background:rgba(255,255,255,.08);border:1px solid rgba(255,255,255,.25);color:#ddd;font-size:12px;line-height:28px;padding-left:10px;margin-bottom:12px}
.field.tall{height:70px}
.consult .btn{display:block;text-align:center;margin-top:22px;height:30px;line-height:30px}

/* features */
.feature{top:610px;width:256px;height:208px;background:var(--teal-bright);color:var(--white);text-align:center;padding:110px 24px 0;font-size:15px;font-weight:600;line-height:22px}
.feature-icon{top:-2px;left:84px;width:88px}
.f1{left:144px}.f2{left:464px}.f3{left:784px}

/* instruments */
.instruments-title{top:868px;left:0;width:1200px}
.instruments-text{left:120px;top:960px;width:420px}
.instruments-media{left:660px;top:938px;width:460px;height:264px;background:linear-gradient(135deg,#f3f5f7,#d7dde2 55%,#eef1f4)}
.instr-btn{left:120px;top:1166px}

/* leasing band */
.leasing{top:1352px;left:0;width:1200px;height:468px;background:var(--teal)}
.leasing h2{position:absolute;top:56px;left:0;width:1200px;text-align:center;color:var(--white);font-size:28px;line-height:38px;font-weight:700}
.leasing-text{left:120px;top:1536px;width:440px}
.leasing-text p.body{color:var(--band-text)}
.leasing-media{left:600px;top:1526px;width:460px;height:210px;background:linear-gradient(160deg,#f4f6f8,#c9d2d9 60%,#3a5aa8 61%,#2c3f78)}
.lease-btn{left:120px;top:1744px}

/* team */
.team-title{top:1900px;left:0;width:1200px}
.member{top:1966px;width:200px;text-align:center}
.member svg{display:block;margin:0 auto}
.member h4{font-size:15px;font-weight:700;margin-top:14px}
.member small{display:block;font-size:11px;color:var(--muted);margin-top:2px}
.member .social{justify-content:center;margin-top:10px;gap:6px}
.member .social span{width:18px;height:18px;background:var(--dark)}
.m1{left:226px}.m2{left:500px}.m3{left:774px}
.dots{left:586px;top:2282px;display:flex;gap:6px}
.dots span{width:7px;height:7px;border-radius:50%;background:#aaa}
.dots span.on{background:var(--dark)}

/* about */
.about{top:2340px;left:0;width:1200px;height:480px;background:var(--teal)}
.about h2{position:absolute;left:120px;top:70px;color:var(--white);font-size:30px;font-weight:700}
.about-text{left:120px;top:2466px;width:440px}
.about-text p.body{color:var(--band-text);margin-bottom:12px}
.about-media{left:640px;top:2400px;width:420px;height:300px;background:radial-gradient(circle at 50% 55%,#5fd0c3 0%,#1c8a82 55%,var(--teal) 75%)}
.about-btn{left:120px;top:2730px}

/* faq */
.faq-title{top:2868px;left:0;width:1200px}
.faq-media{left:120px;top:2940px;width:454px;height:300px;background:linear-gradient(120deg,#dbe6f1,#a9c1d9 60%,#e9eef3)}
.faq-list{left:600px;top:2948px;width:480px}
.faq-item{height:30px;border:1px solid var(--line);margin-bottom:8px;font-size:11px;color:var(--muted);line-height:28px;padding-left:14px;position:relative}
.faq-item::after{content:"";position:absolute;right:12px;top:12px;border-left:4px solid transparent;border-right:4px solid transparent;border-top:5px solid #555}

/* newsletter */
.news-title{top:3290px;left:0;width:1200px;font-size:22px}
.news-sub{top:3334px;left:0;width:1200px;text-align:center;font-size:11px;color:var(--muted)}
.news-form{left:284px;top:3374px;display:flex;gap:12px}
.news-input{width:460px;height:32px;border-bottom:1px solid #bbb;background:#f5f6f7;font-size:11px;color:#999;line-height:32px;padding-left:12px}
.news-form .btn{height:32px;line-height:32px;padding:0 52px}

/* footer */
.site-footer{top:3472px;left:0;width:1200px;height:308px;background:var(--dark)}
.foot-brand{left:120px;top:3510px}
.foot-about{left:120px;top:3556px;width:200px;font-size:12px;line-height:18px;color:var(--foot-text)}
.foot-col{color:var(--foot-text)}
.foot-col h5{font-size:13px;font-weight:600;color:var(--white);margin-bottom:12px}
.foot-col li{list-style:none;font-size:11px;line-height:17px;padding-left:10px;position:relative;color:var(--foot-text)}
.foot-col li::before{content:"";position:absolute;left:0;top:7px;width:4px;height:4px;border-radius:50%;background:var(--foot-text)}
.fc-links{left:360px;top:3504px}
.fc-contact{left:478px;top:3504px;width:260px}
.contact-row{display:flex;font-size:11px;line-height:17px;color:var(--foot-text)}
.contact-row b{font-weight:400;width:64px;flex:none}
.fc-quick{left:804px;top:3504px;width:276px}
.qc-row{display:flex;gap:8px;margin-bottom:8px}
.qc-field{flex:1;height:24px;background:rgba(255,255,255,.08);border:1px solid rgba(255,255,255,.2);font-size:10px;line-height:22px;padding-left:8px;color:#bbb}
.qc-field.tall{height:56px}
.fc-quick .btn{display:block;text-align:center;height:24px;line-height:24px;font-size:11px}
.copyright{left:120px;top:3798px;font-size:11px;color:var(--muted)}
</style>
</head>
<body>

<header class="abs site-header">
  <svg class="abs menu-icon" width="20" height="16" viewBox="0 0 20 16"><rect y="0" width="20" height="2.5" fill="#17a096"/><rect y="6.5" width="20" height="2.5" fill="#17a096"/><rect y="13" width="20" height="2.5" fill="#17a096"/></svg>
  <div class="abs brand"><span class="brand-dot"></span>tarvio</div>
  <div class="abs social header-social"><span class="on"></span><span></span><span></span><span></span><span></span></div>
</header>

<section class="abs hero" role="img" aria-label="Scientist in a white lab coat working at a laboratory bench"></section>
<div class="abs hero-title">YOUR SUCCESS<span>OUR SUPPORT...</span></div>

<form class="abs consult">
  <h3>Free Consultation</h3>
  <div class="field">Name</div>
  <div class="field">Phone</div>
  <div class="field">Email</div>
  <div class="field tall">Message</div>
  <span class="btn">Submit</span>
</form>

<div class="abs feature f1">
  <svg class="abs feature-icon" viewBox="0 0 88 96" height="96"><polygon points="44,2 86,26 86,70 44,94 2,70 2,26" fill="#2b2e34" stroke="#fff" stroke-width="3"/><rect x="28" y="38" width="32" height="24" rx="2" fill="#fff"/><rect x="38" y="32" width="12" height="7" fill="none" stroke="#fff" stroke-width="2"/><rect x="41" y="43" width="6" height="14" fill="#2b2e34"/><rect x="37" y="47" width="14" height="6" fill="#2b2e34"/></svg>
  Worry-free lab equipment FMV/repair coverage
</div>
<div class="abs feature f2">
  <svg class="abs feature-icon" viewBox="0 0 88 96" height="96"><polygon points="44,2 86,26 86,70 44,94 2,70 2,26" fill="#2b2e34" stroke="#fff" stroke-width="3"/><circle cx="44" cy="48" r="16" fill="none" stroke="#fff" stroke-width="3"/><line x1="44" y1="48" x2="52" y2="40" stroke="#fff" stroke-width="3"/></svg>
  Cost-effective lease structures and payment plans
</div>
<div class="abs feature f3">
  <svg class="abs feature-icon" viewBox="0 0 88 96" height="96"><polygon points="44,2 86,26 86,70 44,94 2,70 2,26" fill="#2b2e34" stroke="#fff" stroke-width="3"/><path d="M38 30h12M40 30v14l-10 18h28l-10-18V30" fill="none" stroke="#fff" stroke-width="3"/></svg>
  Knowledge of the laboratory
</div>

<h2 class="abs section-title instruments-title">Instruments &amp; Service</h2>
<div class="abs instruments-text">
  <p class="body">Do you need laboratory equipment leasing programs? Because when capital is limited, purchasing equipment becomes a serious burden. Fortunately there is a solution. Our lab equipment support lets you add instruments with a low monthly fee and flexible terms for every team.</p>
  <p class="body">Plus, when you collaborate with us you get everything you need to run your lab, from routine service to full repair coverage, all in a single affordable package built around your research.</p>
</div>
<div class="abs instruments-media" role="img" aria-label="Group of laboratory instruments including an analyser and a microscope"></div>
<span class="abs btn instr-btn" style="background:var(--teal)">Read More</span>

<section class="abs leasing"><h2>Trusted Company Offering Scientific Equipment Service<br>Plans and Flexible Leases</h2></section>
<div class="abs leasing-text">
  <p class="body">At tarvio, our goal is to ensure the success of your business. Whether you are running a laboratory or other scientific facility, we want to keep you equipped with the best in cutting edge equipment.</p>
  <p class="body">That is why we offer flexible scientific equipment leasing options with worry-free service plans, so you can provide your team with the tools needed to perform at its peak.</p>
</div>
<div class="abs leasing-media" role="img" aria-label="Benchtop laboratory scanner instrument"></div>
<span class="abs btn lease-btn">Read More</span>

<h2 class="abs section-title team-title">Our Team</h2>
<div class="abs member m1">
  <svg width="150" height="170" viewBox="0 0 150 170" role="img" aria-label="Portrait photo of Ren Okada"><defs><linearGradient id="g1" x1="0" y1="0" x2="0" y2="1"><stop offset="0" stop-color="#e6e2dc"/><stop offset="1" stop-color="#8a8f96"/></linearGradient></defs><polygon points="75,4 146,44 146,126 75,166 4,126 4,44" fill="url(#g1)" stroke="#2b2e34" stroke-width="4"/></svg>
  <h4>REN OKADA</h4><small>Lab Relations</small>
  <div class="social"><span></span><span></span><span></span></div>
</div>
<div class="abs member m2">
  <svg width="150" height="170" viewBox="0 0 150 170" role="img" aria-label="Portrait photo of Mark Delaney"><defs><linearGradient id="g2" x1="0" y1="0" x2="0" y2="1"><stop offset="0" stop-color="#dfe4e8"/><stop offset="1" stop-color="#7d8794"/></linearGradient></defs><polygon points="75,4 146,44 146,126 75,166 4,126 4,44" fill="url(#g2)" stroke="#2b2e34" stroke-width="4"/></svg>
  <h4>MARK DELANEY</h4><small>Finance</small>
  <div class="social"><span></span><span></span><span></span></div>
</div>
<div class="abs member m3">
  <svg width="150" height="170" viewBox="0 0 150 170" role="img" aria-label="Portrait photo of Arjun Sethi"><defs><linearGradient id="g3" x1="0" y1="0" x2="0" y2="1"><stop offset="0" stop-color="#ece9e4"/><stop offset="1" stop-color="#5b6470"/></linearGradient></defs><polygon points="75,4 146,44 146,126 75,166 4,126 4,44" fill="url(#g3)" stroke="#2b2e34" stroke-width="4"/></svg>
  <h4>ARJUN SETHI</h4><small>Operations</small>
  <div class="social"><span></span><span></span><span></span></div>
</div>
<div class="abs dots"><span class="on"></span><span></span></div>

<section class="abs about"><h2>About Us</h2></section>
<div class="abs about-text">
  <p class="body">Our mission is to assist laboratories that seek to further scientific innovation. By providing equipment leasing and repair coverage, we aim to accelerate research and relieve laboratories of heavy financial burdens.</p>
  <p class="body">At the rate that science and technology move, researchers should not be slowed down by inaccessible or unaffordable research equipment.</p>
  <p class="body">Our leasing model stands behind this statement, promoting lab financial and operational flexibility.</p>
</div>
<div class="abs about-media" role="img" aria-label="Illustration of laboratory glassware, flasks and a microscope"></div>
<span class="abs btn about-btn">Read More</span>

<h2 class="abs section-title faq-title">Frequently Asked Questios</h2>
<div class="abs faq-media" role="img" aria-label="Researcher looking into a microscope"></div>
<div class="abs faq-list">
  <div class="faq-item">Lorem Ipsum is simply dummy text of the printing</div>
  <div class="faq-item">Lorem Ipsum is simply dummy text of the printing</div>
  <div class="faq-item">Lorem Ipsum is simply dummy text of the printing</div>
  <div class="faq-item">Lorem Ipsum is simply dummy text of the printing</div>
  <div class="faq-item">Lorem Ipsum is simply dummy text of the printing</div>
  <div class="faq-item">Lorem Ipsum is simply dummy text of the printing</div>
  <div class="faq-item">Lorem Ipsum is simply dummy text of the printing</div>
  <div class="faq-item">Lorem Ipsum is simply dummy text of the printing</div>
</div>

<h2 class="abs section-title news-title">Subscribe To Our Newsletter</h2>
<p class="abs news-sub">Be Receive The Latest News And Update</p>
<div class="abs news-form"><div class="news-input">Your E-Mail</div><span class="btn">Submit</span></div>

<footer class="abs site-footer"></footer>
<div class="abs brand foot-brand"><span class="brand-dot"></span>tarvio</div>
<p class="abs foot-about">Lorem Ipsum is simply dummy text of the printing and types offerings the industry.</p>
<div class="abs foot-col fc-links">
  <h5>Quick Link</h5>
  <ul><li>Home</li><li>Services</li><li>Leasing</li><li>Our Team</li><li>About us</li><li>FAQ</li><li>Contact us</li></ul>
</div>
<div class="abs foot-col fc-contact">
  <h5>Contact us</h5>
  <div class="contact-row"><b>Tarvio Inc.</b><span>48 Harbor Lane<br>Suite 310<br>Oakland, CA 94607</span></div>
  <div class="contact-row" style="margin-top:8px"><b>Phone</b><span>(415) 555-0148</span></div>
  <div class="contact-row"><b>E-mail</b><span>info@tarvio.com</span></div>
</div>
<div class="abs foot-col fc-quick">
  <h5>Quick Contact</h5>
  <div class="qc-row"><div class="qc-field">Name</div><div class="qc-field">Phone</div></div>
  <div class="qc-row"><div class="qc-field tall">Message</div></div>
  <span class="btn">Send</span>
</div>
<p class="abs copyright">© Copyright 2019 Tarvio. All Rights Reserved.</p>

</body>
</html>
```